Business cards and Stationary | Lumora Music Events

Hello! We need business cards and stationery for a new small business in the music industry. "Lumora is a high-end music agency which provides an unparalleled level of talent and personalized service to the realm entertainment, corporate events, and luxury weddings. Here is where the classical meets the contemporary and we can bring your vision to life.Keeping a steady finger on the pulse of current trends and consistently raising the bar for industry standards, Lumora continues to rise to the forefront of the music industry, providing the utmost professional, high-end, elegant, and engaging entertainment in Australia and World-Wide."

Target Market(s)

Class A. high profile corporate business.

Industry/Entity Type

Entertainment

Contact Information for Business Card

Lumora Music Events

Clare Yoshinaga
Director | Violinist

Level 7, 41 Caddow Lane
Sydney, 2000

Website: www.lumoramusicevents-demo.net
Phone number: 0455 318 602
Email: clare@lumoramusicevents-demo.net

Font styles to use
Serif
Sans Serif
Script

Colors
feeeee
0355a3
f59296
ffffff

Requirements
Nice to have
• Clean and sophisticated would be perfect.
• If there is a way to include the Instagram without being tacky, that would be awesome
• @lumoramusicevents
• Our website and logo have the following fonts:
• The primary logo is inspired and based on a font called BillionScript but the B is completely hand drawn and the rest is customised a bit to work together cohesively
• Monserrat Light - Is the Music part of the logo and as headers in the site
• Open Sans 300 and 400 (Light or Regular) is used mostly as the body text in the site
• If you want to access the website:
• www.lumoramusicevents-demo.net
• username: client
• password: preview

```html
<!DOCTYPE html>
<html lang="en">
<head>
<meta charset="utf-8">
<title>Lumora Music Events – Business Card</title>
<link rel="stylesheet" href="https://fonts.googleapis.com/css2?family=Montserrat:wght@300;400&display=swap">
<style>
  :root {
    --page: #2a2c31;
    --blush: #fdeeee;
    --coral: #f07b7e;
    --coral-light: #f7a3a5;
    --ink: #b0807b;
  }
  * { box-sizing: border-box; margin: 0; padding: 0; }
  html, body { width: 1200px; height: 1200px; overflow: hidden; background: var(--page); }
  body { font-family: "Montserrat", sans-serif; font-weight: 300; color: var(--ink); }
  .sheet {
    width: 1200px; height: 1200px;
    display: flex; flex-direction: column; align-items: center; justify-content: center; gap: 60px;
  }
  .card {
    position: relative; width: 880px; height: 503px;
    border-radius: 34px; overflow: hidden; background: var(--blush);
  }
  .accent-panel {
    position: absolute; top: 0; right: 0; bottom: 0; width: 300px;
    background: radial-gradient(circle at 30% 30%, var(--coral-light), var(--coral));
  }
  .handle {
    position: absolute; left: 44px; top: 48px;
    font-size: 17px; letter-spacing: 0.04em;
  }
  .brand {
    position: absolute; left: 70px; top: 210px;
    display: flex; align-items: center; gap: 18px;
  }
  .brand-dot { width: 16px; height: 16px; border-radius: 50%; background: var(--ink); flex: none; }
  .brand-name { font-size: 52px; letter-spacing: 0.05em; line-height: 1; white-space: nowrap; }
  .contact-list {
    position: absolute; left: 70px; top: 260px;
    list-style: none; display: flex; flex-direction: column; gap: 16px;
    font-size: 21px; letter-spacing: 0.01em;
  }
  .contact-list li { display: flex; align-items: center; gap: 18px; white-space: nowrap; }
  .contact-icon { width: 20px; height: 20px; flex: none; fill: var(--ink); }
</style>
</head>
<body>
<main class="sheet">

  <section class="card card-front" aria-label="Business card front">
    <div class="accent-panel" role="img" aria-label="Coral curved decorative area"></div>
    <p class="handle">@lumoramusicevents</p>
    <p class="brand"><span class="brand-dot"></span><span class="brand-name">Lumora Music</span></p>
  </section>

  <section class="card card-back" aria-label="Business card back">
    <div class="accent-panel" role="img" aria-label="Coral curved decorative area"></div>
    <ul class="contact-list">
      <li>
        <svg class="contact-icon" viewBox="0 0 24 24" aria-hidden="true"><path d="M6.6 10.8a15 15 0 0 0 6.6 6.6l2.2-2.2a1 1 0 0 1 1-.25 11.4 11.4 0 0 0 3.6.57 1 1 0 0 1 1 1V20a1 1 0 0 1-1 1A17 17 0 0 1 3 4a1 1 0 0 1 1-1h3.5a1 1 0 0 1 1 1c0 1.25.2 2.45.57 3.6a1 1 0 0 1-.25 1Z"/></svg>
        <span>0455 318 602</span>
      </li>
      <li>
        <svg class="contact-icon" viewBox="0 0 24 24" aria-hidden="true"><path d="M2 5h20v14H2Z M2 5l10 8 10-8" fill="var(--ink)" stroke="var(--blush)" stroke-width="1.5"/></svg>
        <span>contact@lumoramusicevents-demo.net</span>
      </li>
      <li>
        <svg class="contact-icon" viewBox="0 0 24 24" aria-hidden="true"><circle cx="12" cy="12" r="10"/><path d="M2 12h20M12 2c3 3 3 17 0 20M12 2c-3 3-3 17 0 20" fill="none" stroke="var(--blush)" stroke-width="1.4"/></svg>
        <span>www.lumoramusicevents-demo.net</span>
      </li>
      <li>
        <svg class="contact-icon" viewBox="0 0 24 24" aria-hidden="true"><path d="M12 2a7 7 0 0 0-7 7c0 5 7 13 7 13s7-8 7-13a7 7 0 0 0-7-7Z"/></svg>
        <span>Level 7, 41 Caddow Lane, Sydney, 2000</span>
      </li>
    </ul>
  </section>

</main>
</body>
</html>
```